Company: Plant Grillhouse
We make Plant Grillhouse more popular.
We are producing cooking books and spices.
For our spices (5 sorts) we need an label design.
Measurments of the label: 255mm x 55mm ( small changes of the exact measurements could follow in the next few days)
Name of the sorts:
- Sunny Zestpepper (Yellow)
- Desert Caravan (Orange/Brown)
- Charred Ember-Rub (Red)
- Charm of Tuscany (Green)
- Bold Shallotine (Black)
Attached you can find our main brand.
You can see we try to be clean and simple.
The package is a square glass with a cork closure
4 Side.
Side 1: Logo and Spice Name
Side 2: Incredients and Company Information
Side 3: Nice grphic that matches the sort of the spice
Side 4: Short story of the product and its added value
We look forward to cool suggestions.
Regards
Tobias
We want make the vegan lifestyle more cool.
So therefore don`t choose a too much ecological way, that is not up to date.

```html
<!DOCTYPE html>
<html lang="de">
<head>
<meta charset="utf-8">
<title>Charm of Tuscany – Gewürzetikett</title>
<link rel="stylesheet" href="https://fonts.googleapis.com/css2?family=Bebas+Neue&family=Montserrat:wght@400;700&display=swap">
<style>
  :root {
    --label-green: #adf56f;
    --herb-green: #7fc24a;
    --ink: #111111;
    --band-black: #000000;
    --paper: #ffffff;
  }
  * { margin: 0; padding: 0; box-sizing: border-box; }
  html, body { width: 1200px; height: 259px; overflow: hidden; background: var(--paper); }
  .label {
    position: relative;
    width: 1200px;
    height: 259px;
    background: var(--paper);
    font-family: "Montserrat", sans-serif;
    color: var(--ink);
  }
  .label__panel {
    position: absolute;
    left: 0; top: 0;
    width: 1200px; height: 208px;
    background: var(--label-green);
  }
  .herb-illustration {
    position: absolute;
    left: 0; top: 0;
    width: 376px; height: 208px;
    background: linear-gradient(120deg, var(--label-green) 0%, var(--herb-green) 55%, var(--label-green) 100%);
    opacity: 0.85;
  }
  .herb-illustration--edge {
    left: 1170px; top: 36px;
    width: 30px; height: 102px;
    border-radius: 30px 0 0 30px;
  }
  .spice-title {
    position: absolute;
    left: 376px; top: 54px;
    width: 270px;
    text-align: center;
    font-family: "Bebas Neue", sans-serif;
    font-size: 60px;
    line-height: 54px;
    letter-spacing: 0.17em;
    color: var(--ink);
  }
  .story {
    position: absolute;
    left: 640px; top: 24px;
    width: 258px;
    text-align: center;
  }
  .column-heading {
    font-size: 10px;
    font-weight: 700;
    letter-spacing: 0.2em;
    text-transform: uppercase;
    margin-bottom: 14px;
  }
  .story__text {
    font-size: 10.5px;
    line-height: 16px;
    letter-spacing: 0.15em;
  }
  .nutrition {
    position: absolute;
    left: 966px; top: 24px;
    width: 200px;
  }
  .nutrition .column-heading { text-align: center; }
  .nutrition__table { list-style: none; width: 193px; margin-left: 5px; }
  .nutrition__row {
    display: flex;
    font-size: 10.5px;
    line-height: 16px;
    letter-spacing: 0.13em;
    text-transform: uppercase;
  }
  .nutrition__leader {
    flex: 1;
    overflow: hidden;
    white-space: nowrap;
    letter-spacing: 0.05em;
  }
  .nutrition__leader::after {
    content: "..................................................................";
  }
  .company-line {
    margin-top: 16px;
    text-align: center;
    font-size: 10.5px;
    font-weight: 700;
    letter-spacing: 0.2em;
  }
  .brand-band {
    position: absolute;
    left: 0; top: 211px;
    width: 1200px; height: 46px;
    background: var(--band-black);
  }
  .brand-mark {
    position: absolute;
    left: 394px; top: 0;
    height: 46px;
    display: flex;
    align-items: center;
    gap: 9px;
    color: var(--paper);
    font-weight: 700;
    font-size: 14px;
    letter-spacing: 0.01em;
  }
  .brand-mark__dot {
    width: 30px; height: 30px;
    border-radius: 50%;
    background: var(--paper);
  }
</style>
</head>
<body>
  <main class="label">
    <section class="label__panel">
      <div class="herb-illustration" role="img" aria-label="Line drawing of basil, peppers, garlic, seeds and rosemary"></div>
      <div class="herb-illustration herb-illustration--edge" role="img" aria-label="Line drawing of basil leaves at the label edge"></div>

      <h1 class="spice-title">Charm<br>of Tuscany</h1>

      <article class="story">
        <h2 class="column-heading">Zestpepper-Gewürz:</h2>
        <p class="story__text">Geschichte des Gewürzes. Lorem ipsum dolor sit amet, consetetur sadipscing elitr, sed diam nonumy eirmod tempor invidunt ut labore et dolore magna aliquyam erat, sed diam voluptua.<br>sed diam nonumy eirmod tempor invidunt ut magna aliquyam erat, sed diam voluptua</p>
      </article>

      <section class="nutrition">
        <h2 class="column-heading">Inhaltsstoffe:</h2>
        <ul class="nutrition__table">
          <li class="nutrition__row"><span>Energie</span><span class="nutrition__leader"></span><span>KJ/KCAL</span></li>
          <li class="nutrition__row"><span>Fett</span><span class="nutrition__leader"></span><span>G</span></li>
          <li class="nutrition__row"><span>Kohlenhydrate</span><span class="nutrition__leader"></span><span>G</span></li>
          <li class="nutrition__row"><span>Davon Zucker</span><span class="nutrition__leader"></span><span>G</span></li>
          <li class="nutrition__row"><span>Ballaststoffe</span><span class="nutrition__leader"></span><span>G</span></li>
          <li class="nutrition__row"><span>Eiweiss</span><span class="nutrition__leader"></span><span>G</span></li>
          <li class="nutrition__row"><span>Salz</span><span class="nutrition__leader"></span><span>G</span></li>
        </ul>
        <p class="company-line">PLANT GRILLHOUSE GMBH</p>
      </section>
    </section>

    <footer class="brand-band">
      <div class="brand-mark">
        <span class="brand-mark__dot"></span>
        <span class="brand-mark__name">PLANT GRILLHOUSE</span>
      </div>
    </footer>
  </main>
</body>
</html>
```